Flyer for Corvane Visual - Design Agency

We need a 4-page square flyer measuring 14.8x14.8cm per page, to fold out, for a design agency targeting small businesses.
The design should be very modern. There shouldn't be too much content visible.
The background should be black. The color of the logo (attached) can also be used. The content is also attached and divided per page. We are open to alternative suggestions regarding the division.

```html
<!DOCTYPE html>
<html lang="de">
<head>
<meta charset="utf-8">
<title>Corvane Visual – Faltflyer</title>
<link rel="stylesheet" href="https://fonts.googleapis.com/css2?family=Saira+Extra+Condensed:wght@300;600&family=Arimo:wght@400&display=swap">
<style>
  :root {
    --paper: #ffffff;
    --ink: #070708;
    --teal: #8fd3d8;
    --grey-head: #a3a3a6;
    --grey-text: #c9c9cc;
    --grey-soft: #9a9a9e;
    --diamond: #222223;
    --display: "Saira Extra Condensed", "Arial Narrow", sans-serif;
    --body: "Arimo", Arial, sans-serif;
  }
  * { box-sizing: border-box; margin: 0; padding: 0; }
  html, body { width: 1200px; height: 1200px; overflow: hidden; background: var(--paper); }
  .canvas { position: relative; width: 1200px; height: 1200px; }

  .spread { position: absolute; left: 119px; width: 962px; height: 481px; background: var(--ink); overflow: hidden; }
  .spread--outside { top: 77px; }
  .spread--inside { top: 600px; }

  /* outside */
  .line-pattern { position: absolute; top: 0; height: 100%; }
  .line-pattern--outside {
    left: 266px; width: 420px;
    background: radial-gradient(ellipse at 50% 50%, #050505 0 18%, #1c1c1e 45%, #0c0c0d 75%, var(--ink) 100%);
  }
  .tagline { position: absolute; left: 64px; top: 152px; font-family: var(--display); font-weight: 300; font-size: 21px; line-height: 22px; color: var(--teal); }
  .contact { position: absolute; left: 64px; top: 213px; font-family: var(--display); font-weight: 300; font-size: 13px; color: var(--grey-soft); }
  .contact__invite { margin-bottom: 12px; }
  .contact__list { list-style: none; }
  .contact__item { display: flex; align-items: flex-start; gap: 6px; line-height: 14px; }
  .contact__item svg { width: 10px; height: 10px; margin-top: 2px; flex: none; fill: var(--grey-soft); }
  .contact__owners { margin-top: 15px; }

  .wordmark { position: absolute; left: 790px; top: 92px; font-family: var(--display); font-weight: 300; font-size: 34px; line-height: 30px; color: var(--teal); text-transform: lowercase; }
  .claim-dash { position: absolute; left: 873px; top: 291px; width: 22px; height: 4px; background: var(--teal); }
  .claim { position: absolute; right: 62px; top: 302px; text-align: right; font-family: var(--display); font-weight: 600; font-size: 28px; line-height: 28px; color: var(--grey-head); }

  /* inside */
  .diamond { position: absolute; left: 0; top: 0; }
  .line-pattern--inside {
    left: 316px; width: 342px;
    background: linear-gradient(100deg, var(--ink) 0%, #151516 35%, #3a3a3c 70%, #111112 90%, var(--ink) 100%);
  }
  .illustration {
    position: absolute; left: 0; top: 232px; width: 290px; height: 249px;
    background: linear-gradient(135deg, #0b5fa0 0%, #9fd9f0 40%, #ee4f99 65%, #ffe600 100%);
  }
  .headline { position: absolute; left: 13px; top: 28px; font-family: var(--display); font-weight: 600; font-size: 29px; line-height: 28px; color: var(--teal); }
  .intro { position: absolute; left: 13px; top: 131px; font-family: var(--body); font-size: 11.5px; line-height: 15px; color: var(--grey-text); }

  .services-title { position: absolute; left: 669px; top: 28px; font-family: var(--display); font-weight: 600; font-size: 28px; color: var(--grey-head); }
  .service { position: absolute; left: 652px; display: flex; gap: 10px; }
  .service__icon { width: 38px; height: 38px; margin-top: 4px; border: 1.5px solid #cfcfd2; flex: none; }
  .service__name { font-family: var(--display); font-weight: 600; font-size: 17px; line-height: 17px; color: var(--teal); }
  .service__text { font-family: var(--body); font-size: 11.5px; line-height: 15px; color: var(--grey-text); }

  .reasons { position: absolute; left: 657px; top: 387px; font-family: var(--body); font-size: 9.5px; line-height: 12.5px; color: var(--grey-text); }
  .reasons__title { padding-left: 7px; }
  .reasons__list { list-style: none; }
  .reasons__item { position: relative; padding-left: 7px; }
  .reasons__item::before { content: ""; position: absolute; left: 0; top: 4px; width: 4px; height: 4px; background: var(--teal); transform: rotate(45deg); }
</style>
</head>
<body>
<main class="canvas">

  <section class="spread spread--outside" aria-label="Außenseite">
    <div class="line-pattern line-pattern--outside" role="img" aria-label="Dekoratives Muster aus feinen grauen Wellenlinien"></div>

    <p class="tagline">Corvane Visual – Designs,<br>die wirken. Marken, die bleiben.</p>

    <div class="contact">
      <p class="contact__invite">Kontaktiere uns für eine kostenlose Beratung!</p>
      <ul class="contact__list">
        <li class="contact__item"><svg viewBox="0 0 10 10"><path d="M0 2h10v6H0z M0 2l5 3.5L10 2" fill="none" stroke="#9a9a9e" stroke-width="1.2"/><path d="M0 2h10L5 5.5z"/></svg>studio@corvanevisual.de</li>
        <li class="contact__item"><svg viewBox="0 0 10 10"><path d="M0 4q5-3 10 0v2H7.5V5h-5v1H0z"/></svg>+49 000 48213</li>
        <li class="contact__item"><svg viewBox="0 0 10 10"><path d="M5 0a3.5 3.5 0 0 1 3.5 3.5C8.5 6 5 10 5 10S1.5 6 1.5 3.5A3.5 3.5 0 0 1 5 0zm0 2a1.5 1.5 0 1 0 0 3 1.5 1.5 0 0 0 0-3z"/></svg>Lindenhofweg 9<br>60311 Frankfurt</li>
      </ul>
      <p class="contact__owners">Inhaber: Jana Ostrow &amp; Felix Brandt</p>
    </div>

    <p class="wordmark">corvane<br>visual</p>

    <div class="claim-dash"></div>
    <p class="claim">Dein Unternehmen.<br>Dein Stil.<br>Unser Design.</p>
  </section>

  <section class="spread spread--inside" aria-label="Innenseite">
    <svg class="diamond" width="300" height="300" viewBox="0 0 300 300" aria-hidden="true">
      <polygon points="119,-27 265,119 119,265 -27,119" fill="var(--diamond)"/>
    </svg>
    <div class="line-pattern line-pattern--inside" role="img" aria-label="Dekoratives Muster aus feinen weißen Wellenlinien"></div>
    <div class="illustration" role="img" aria-label="Geometrische Illustration aus Kreisen und Dreiecken in Blau, Pink, Gelb und Weiß"></div>

    <h1 class="headline">Modern, mutig, markant – Corvane Visual<br>gestaltet die Zukunft<br>deines Unternehmensauftritts.</h1>
    <p class="intro">Wir machen aus Ideen visuelle Erlebnisse und sorgen dafür,<br>dass deine Marke im Gedächtnis bleibt.</p>

    <h2 class="services-title">Unsere Leistungen:</h2>

    <div class="service" style="top:78px">
      <div class="service__icon" role="img" aria-label="Symbol gestapelte Ebenen"></div>
      <div><p class="service__name">Next-Level Flyer</p><p class="service__text">Nicht nur Papier, sondern deine Botschaft<br>im perfekten Look.</p></div>
    </div>
    <div class="service" style="top:147px">
      <div class="service__icon" role="img" aria-label="Symbol Würfel"></div>
      <div><p class="service__name">Corporate Identity</p><p class="service__text">Ein Design, das deine Marke<br>spricht – individuell, stark, unvergesslich.</p></div>
    </div>
    <div class="service" style="top:212px">
      <div class="service__icon" role="img" aria-label="Symbol Drucker"></div>
      <div><p class="service__name">Digital &amp; Print</p><p class="service__text">Ob Social Media Grafiken oder klassisches<br>Printdesign – wir sind da, wo du uns brauchst.</p></div>
    </div>
    <div class="service" style="top:284px">
      <div class="service__icon" role="img" aria-label="Symbol Typografie"></div>
      <div><p class="service__name">Alles aus einer Hand</p><p class="service__text">Logo, Farben, Typografie, Flyer und vieles<br>mehr – wir bauen das Fundament für<br>deinen Erfolg.</p></div>
    </div>

    <div class="reasons">
      <p class="reasons__title">Warum wir?</p>
      <ul class="reasons__list">
        <li class="reasons__item">Dein Style, unser Know-how: Wir kombinieren deine<br>Vision mit moderner Ästhetik.</li>
        <li class="reasons__item">Persönlicher Service – Wir hören zu und setzen um,<br>was dich einzigartig macht</li>
        <li class="reasons__item">Flexible Lösungen für die unterschiedlichsten Anforderungen</li>
      </ul>
    </div>
  </section>

</main>
</body>
</html>
```